Driver License Monitoring Application Marketing Website

We need a new web design for our web application. The product is called "PermitSentry." We provide a driver license monitoring service to companies and local government bodies with driver fleets. Our current website is available at www.PermitSentry-demo.net.

I prefer a clean, single-page design with good SEO. Attached are some PDFs with data about the project.

Target Market(s)

Companies with driver fleets, local government.

Industry/Entity Type

Government

Coding

Coded - Design and coding required

Number of Pages Required

1 page

Colors
000000

Requirements
Must have
• Content from current www.PermitSentry-demo.net and attached PDFs.
Nice to have
• Prefer a simple Bootstrap or similar design for easy editing.
• Room for a simple video explanation of how the product works (we don't have an actual video yet)

```html
<!DOCTYPE html>
<html lang="en">
<head>
<meta charset="utf-8">
<title>PermitSentry – Driver License Monitoring</title>
<link rel="stylesheet" href="https://fonts.googleapis.com/css2?family=Montserrat:wght@700;800&family=Kreon:wght@300;400;700&family=Open+Sans:wght@400;600&display=swap">
<style>
:root{
  --teal:#2bbaa0;
  --teal-dark:#1f9a84;
  --ink:#ffffff;
  --nav:#1e1e1e;
  --welcome:#1e1e1e;
  --industries:#2e2e2e;
  --footer:#232323;
  --bottom:#1a1a1a;
  --muted:#8a8a8a;
  --dim:#6a6a6a;
  --panel:#3a3a3a;
  --panel-light:#555555;
  --field:#2c2c2c;
}
*{margin:0;padding:0;box-sizing:border-box}
html,body{width:1200px;height:2594px;overflow:hidden;background:var(--nav)}
body{font-family:"Kreon",Georgia,serif;color:var(--ink);position:relative}
.display{font-family:"Montserrat",Arial,sans-serif;font-weight:800;text-transform:uppercase;letter-spacing:1px}

/* nav */
.site-nav{position:absolute;top:0;left:0;width:1200px;height:93px;background:var(--nav)}
.brand{position:absolute;left:47px;top:24px;font-family:"Kreon",serif;font-weight:700;font-size:36px;line-height:44px;color:var(--ink);letter-spacing:3px}
.menu{position:absolute;right:45px;top:36px;display:flex;gap:25px;list-style:none;font-family:"Open Sans",sans-serif;font-size:13.5px;text-transform:uppercase}
.menu li{color:#e6e6e6}
.menu li.active{color:var(--teal)}

/* hero */
.hero{position:absolute;top:93px;left:0;width:1200px;height:728px;overflow:hidden}
.hero-photo{position:absolute;inset:0;background:radial-gradient(ellipse at 50% 40%,#6a6a6a 0%,#3e3e3e 55%,#222 100%)}
.hero-title{position:absolute;top:58px;width:100%;text-align:center;font-size:78px;letter-spacing:3px}
.hero-lead{position:absolute;top:178px;width:100%;text-align:center;font-size:19px;line-height:29px;text-transform:uppercase;letter-spacing:.5px}
.btn{position:absolute;background:var(--teal);color:#fff;text-align:center;border-radius:3px;box-shadow:0 4px 0 var(--teal-dark);font-family:"Montserrat",sans-serif;font-weight:700;text-transform:uppercase}
.btn-more{width:204px;height:62px;padding-top:10px;font-size:19px;letter-spacing:1.5px;line-height:21px}
.btn-more small{display:block;font-family:"Kreon",serif;font-weight:400;font-size:15px;letter-spacing:.5px;text-transform:none}
.screen{position:absolute;background:linear-gradient(180deg,#f4f4f4,#dcdcdc)}
.screen-main{left:268px;top:377px;width:666px;height:351px;box-shadow:0 0 30px rgba(0,0,0,.6)}
.screen-side{top:434px;width:161px;height:294px;opacity:.45}
.social{position:absolute;right:0;top:76px;width:55px}
.social span{display:flex;align-items:center;justify-content:center;width:55px;height:55px;background:#5a5a5a;border-bottom:1px solid #666}
.social span:nth-child(even){background:#6e6e6e}
.search-tab{position:absolute;right:0;top:505px;width:55px;height:56px;background:#2a2a2a;display:flex;align-items:center;justify-content:center}

/* welcome */
.welcome{position:absolute;top:821px;left:0;width:1200px;height:695px;background:var(--welcome);text-align:center}
.welcome-title{position:absolute;top:58px;width:100%;font-size:53px;line-height:60px;letter-spacing:2px}
.welcome-brand{position:absolute;top:113px;width:100%;font-size:34px;line-height:40px;font-weight:700;letter-spacing:3px}
.tabs{position:absolute;left:202px;top:187px;width:797px;height:69px;background:linear-gradient(#4a4a4a,#343434);border-radius:3px;display:flex;font-family:"Open Sans",sans-serif;font-size:22px;align-items:center}
.tab{width:190px;color:#eee}
.tab.active{position:relative;width:235px;height:69px;line-height:69px;color:#fff;background:var(--teal);clip-path:polygon(0 0,88% 0,100% 50%,88% 100%,0 100%,6% 50%)}
.section-head{position:absolute;top:314px;width:100%;font-size:31px}
.section-head .soft{color:#8a8a8a}
.tagline{position:absolute;top:406px;width:100%;font-size:20px}
.intro{position:absolute;top:464px;left:45px;width:1110px;font-size:16px;line-height:30px;color:var(--dim);font-weight:300}
.intro b{color:#fff;font-weight:700}

/* industries */
.industries{position:absolute;top:1516px;left:0;width:1200px;height:578px;background:var(--industries)}
.industries-title{position:absolute;top:50px;width:100%;text-align:center;font-size:32px}
.categories{position:absolute;left:45px;top:123px;width:284px;border-radius:3px;overflow:hidden}
.cat-head{height:66px;background:var(--teal);padding:0 24px;display:flex;align-items:center;justify-content:space-between;font-family:"Montserrat",sans-serif;font-weight:700;font-size:17px}
.cat{height:77px;background:var(--panel-light);border-top:1px solid #444;display:flex;align-items:center;padding:0 20px;font-family:"Open Sans",sans-serif;font-size:16px;color:#eee}
.cat.current{background:var(--panel);color:#888}
.cat .ico{width:36px;height:36px;margin-right:14px}
.cat .dot{margin-left:auto;width:20px;height:20px;border-radius:50%;background:#fff}
.feature{position:absolute;left:363px;top:123px;width:792px;height:375px;border-radius:4px;overflow:hidden}
.feature-photo{position:absolute;inset:0;background:linear-gradient(120deg,#e8e8e8 0%,#9a9a9a 35%,#6a6a6a 60%,#bdbdbd 100%)}
.feature-cap{position:absolute;left:0;bottom:0;width:100%;height:176px;background:rgba(20,20,20,.82);padding:14px 50px}
.feature-cap h3{font-size:32px}
.feature-cap h3 span{color:#9a9a9a}
.feature-cap p{font-size:15px;line-height:20px;color:#888;width:690px;margin-top:6px}
.btn-small{position:static;display:inline-block;margin-top:12px;width:148px;height:38px;line-height:38px;font-size:15px;letter-spacing:1.5px}

/* footer */
.site-footer{position:absolute;top:2094px;left:0;width:1200px;height:434px;background:var(--footer)}
.col{position:absolute;top:32px}
.col h4{font-size:26px;line-height:34px;margin-bottom:30px;letter-spacing:.5px}
.address{font-size:12px;line-height:26.5px;color:#ddd;margin-top:10px}
.links{list-style:none;width:255px}
.links li{font-size:13px;color:#888;height:38px;line-height:38px;border-bottom:1px solid #3a3a3a}
.links li:first-child{color:#fff}
.links li::before{content:"› ";color:#ccc}
.tweet{font-size:13px;line-height:23px;color:#777;width:238px;margin-bottom:24px}
.tweet b{color:#fff}
.field{width:258px;height:38px;background:var(--field);margin-bottom:11px;font-size:13px;color:#ccc;padding:10px 12px}
.field.msg{height:86px}
.btn-submit{position:static;display:block;width:149px;height:38px;line-height:38px;font-size:14px;letter-spacing:2px;margin-top:14px}
.bottom-bar{position:absolute;top:2528px;left:0;width:1200px;height:66px;background:var(--bottom);border-top:1px solid #333;padding:30px 43px;font-size:13px;color:#888}
</style>
</head>
<body>

<header class="site-nav">
  <div class="brand">PermitSentry</div>
  <ul class="menu">
    <li class="active">Home</li><li>License Monitoring</li><li>About Us</li><li>Contact</li><li>Client Login</li>
  </ul>
</header>

<section class="hero">
  <div class="hero-photo" role="img" aria-label="Blurred black and white photo of highway traffic"></div>
  <h1 class="hero-title display">Online Access</h1>
  <p class="hero-lead">Review your fleet status on demand. Get email alerts when license problems<br>arise. Track your drivers' licenses proactively.</p>
  <div class="btn btn-more" style="left:498px;top:267px">More Info<small>track your fleet</small></div>
  <div class="screen screen-side" style="left:107px" role="img" aria-label="Faded view of the application dashboard"></div>
  <div class="screen screen-side" style="left:934px" role="img" aria-label="Faded view of the application dashboard"></div>
  <div class="screen screen-main" role="img" aria-label="Application dashboard showing a license status summary and activity history"></div>
  <div class="social">
    <span><svg width="14" height="14"><rect x="2" y="2" width="10" height="10" fill="none" stroke="#bbb" stroke-width="2"/></svg></span>
    <span><svg width="14" height="14"><circle cx="7" cy="7" r="5" fill="#bbb"/></svg></span>
    <span><svg width="14" height="14"><rect x="3" y="3" width="8" height="8" fill="#bbb"/></svg></span>
    <span><svg width="14" height="14"><circle cx="7" cy="7" r="5" fill="none" stroke="#bbb" stroke-width="2"/></svg></span>
    <span><svg width="18" height="14"><rect x="1" y="2" width="16" height="10" fill="none" stroke="#bbb" stroke-width="1.5"/><path d="M1 2l8 6 8-6" fill="none" stroke="#bbb" stroke-width="1.5"/></svg></span>
    <span><svg width="14" height="14"><circle cx="3" cy="11" r="2" fill="#bbb"/><path d="M2 6a6 6 0 016 6M2 1a11 11 0 0111 11" fill="none" stroke="#bbb" stroke-width="2"/></svg></span>
  </div>
  <div class="search-tab"><svg width="20" height="20"><circle cx="8" cy="8" r="6" fill="none" stroke="#fff" stroke-width="2.5"/><path d="M12.5 12.5l6 6" stroke="#fff" stroke-width="3"/></svg></div>
</section>

<section class="welcome">
  <h2 class="welcome-title display">Welcome To</h2>
  <div class="welcome-brand">PermitSentry</div>
  <nav class="tabs">
    <div class="tab active">What We Do</div>
    <div class="tab" style="width:170px">Commercial</div>
    <div class="tab" style="width:210px">Government</div>
    <div class="tab" style="width:170px">About Us</div>
  </nav>
  <h2 class="section-head display">Track Your <span class="soft">Fleet for Safety</span> and Performance</h2>
  <p class="tagline">Monitor your drivers electronically, twenty-four hours a day.</p>
  <p class="intro">How many of your drivers currently have a suspended license? The answer may surprise you. Driving with a suspended license is the most commonly committed offense in America. In 2011, over <b>1.8 million</b> licenses got suspended in Florida. With just over <b>15 million</b> drivers, that's <b>12%</b> of all licensed Florida drivers.</p>
  <div class="btn btn-more" style="left:498px;top:562px">More Info<small>track your fleet</small></div>
</section>

<section class="industries">
  <h2 class="industries-title display">Industries</h2>
  <div class="categories">
    <div class="cat-head">Catagories<svg width="18" height="18"><circle cx="7" cy="7" r="5" fill="none" stroke="#fff" stroke-width="2.5"/><path d="M11 11l5 5" stroke="#fff" stroke-width="3"/></svg></div>
    <div class="cat current"><svg class="ico"><rect x="6" y="8" width="12" height="26" fill="#666"/><rect x="20" y="14" width="12" height="20" fill="#666"/></svg>Commercial Sector<svg class="dot" viewBox="0 0 20 20" style="background:none"><circle cx="10" cy="10" r="10" fill="#888"/><path d="M5 10l4 4 6-7" fill="none" stroke="#3a3a3a" stroke-width="2.5"/></svg></div>
    <div class="cat"><svg class="ico"><rect x="7" y="6" width="22" height="24" rx="3" fill="#222"/><rect x="10" y="10" width="16" height="8" fill="#777"/><circle cx="12" cy="32" r="2.5" fill="#222"/><circle cx="24" cy="32" r="2.5" fill="#222"/></svg>School Districts<span class="dot"></span></div>
    <div class="cat"><svg class="ico"><path d="M4 14L18 5l14 9z" fill="#222"/><rect x="7" y="16" width="3" height="14" fill="#222"/><rect x="14" y="16" width="3" height="14" fill="#222"/><rect x="20" y="16" width="3" height="14" fill="#222"/><rect x="27" y="16" width="3" height="14" fill="#222"/><rect x="4" y="31" width="28" height="3" fill="#222"/></svg>Government<span class="dot"></span></div>
    <div class="cat"><svg class="ico"><circle cx="18" cy="22" r="12" fill="#222"/><rect x="14" y="5" width="8" height="6" fill="#222"/><text x="18" y="27" fill="#777" font-size="14" text-anchor="middle" font-family="Arial">$</text></svg>Insurance Industry<span class="dot"></span></div>
  </div>
  <div class="feature">
    <div class="feature-photo" role="img" aria-label="Black and white photo of a box truck on a road at sunset"></div>
    <div class="feature-cap">
      <h3 class="display">Commercial <span>Sector</span></h3>
      <p>The private sector is fraught with risk. Having an unlicensed or unqualified driver poses an extreme hazard for companies on the road.</p>
      <div class="btn btn-small">More Info</div>
    </div>
  </div>
</section>

<footer class="site-footer">
  <div class="col" style="left:43px">
    <h4 class="display">Contact</h4>
    <p class="address">Harbourline Fleet Services Pty Ltd.<br><br>(Main Office / Head Office)<br>Level 4, Suite 402 / 118 Example Street,<br>Brookvale, VIC 3999<br>Phone: (03) 5550 104<br>(Second Office)<br>Shop 2/410 Sample Road,<br>Harlow QLD 4999<br>(07) 5550 1982</p>
  </div>
  <div class="col" style="left:330px">
    <h4 class="display">Quick Links</h4>
    <ul class="links" style="margin-top:-6px">
      <li>Lorem ipsum dolor sit</li><li>Amet consectetur</li><li>Praesent vel sem id</li><li>Curabitur hendrerit est</li><li>Aliquam eget erat nec sapien</li><li>Cras id augue nunc</li><li>Sed a nulla urna</li>
    </ul>
  </div>
  <div class="col" style="left:612px">
    <h4 class="display">Latest Tweets</h4>
    <p class="tweet"><b>@namehere</b> Justoid nonummy laoreet phasellent penatoque in antesque pellus elis eget tincidunt. Nequatdui laoreum justo a non tellus laoremut vitae doloreet i day ago</p>
    <p class="tweet"><b>@namehere</b> Justoid nonummy laoreet phasellent penatoque in antesque pellus elis eget tincidunt. Nequatdui laoreum justo a non tellus laoremut vitae doloreet i day ago</p>
  </div>
  <div class="col" style="left:897px">
    <h4 class="display">Contact Us</h4>
    <div class="field">Full Name</div>
    <div class="field">Email Address</div>
    <div class="field">Subject</div>
    <div class="field msg">Message</div>
    <div class="btn btn-submit">Submit</div>
  </div>
</footer>

<div class="bottom-bar">Copyright © 2015 PermitSentry-demo.net - All Rights Reserved</div>

</body>
</html>
```